Envelope and Stationary

I need an envelope and stationary package for my non-profit. I need to be able to download these, print, and use.

I am attached the logos, color files, and information I want on envelope and stationary.

The letter must have room on the left margin to put the list of names, Board Members, etc... I will attach a sample.

What I am looking for is to jazz this up a little bit. The Tobin Vale Children's Foundation is promotes physical fitness in children through after school programs.

Once this project is done, I need a powerpoint template, business cards, and many other pieces.

Please help me make my envelopes and letterhead standout from everyone else.

Target Market(s)

Donors, Community citizens, and prospective partners.

Industry/Entity Type

Fitness

Requirements
Must have
• 1) Logo - see attached
2) Mission Statement - "The MISSION of the TOBIN VALE FOUNDATION is to provide after school enrichment, health, and fitness programs in a safe and nurturing environment."
3) Contact information
4) Space on left Margin for Board of Directors (this space will be available for edits to add/subtract names).

5) See sample letter head: The logo and address is too small and barely visible.

6) PO BOX 315927 * Harlow Bay, Maine 04915
Phone: 877-(TVF)-2815
Email: community@tvfyouth.org
Web: www.tvfyouth.org
Nice to have
• Logo and colors have some feel or scheme across top. Something that makes the letterhead and envelope stand out.

```html
<!DOCTYPE html>
<html lang="en">
<head>
<meta charset="utf-8">
<title>Tobin Vale Children's Foundation — Letterhead and Envelope</title>
<link rel="stylesheet" href="https://fonts.googleapis.com/css2?family=Arimo:wght@400;700&family=Caveat:wght@400&display=swap">
<style>
  :root {
    --stage: #000000;
    --paper: #ffffff;
    --paper-edge: #ececec;
    --navy: #0f3f6e;
    --navy-fade: #ffffff;
    --red: #c8202e;
    --ink: #4a4a4a;
    --ink-strong: #333333;
    --script: #2d4f86;
    --on-colour: #ffffff;
  }
  * { margin: 0; padding: 0; box-sizing: border-box; }
  html, body {
    width: 1200px; height: 1000px; overflow: hidden;
    background: var(--stage);
  }
  .stage { position: relative; width: 1200px; height: 1000px; }
  address { font-style: normal; }

  .sheet {
    position: absolute;
    background: linear-gradient(90deg, var(--paper-edge) 0%, var(--paper) 25%, var(--paper) 100%);
    font-family: "Arimo", Arial, sans-serif;
    color: var(--ink);
  }

  /* Letterhead */
  .letterhead { left: 52px; top: 97px; width: 530px; height: 685px; }

  .brand-panel {
    position: absolute;
    background: linear-gradient(180deg, var(--navy) 0%, var(--navy) 52%, var(--navy-fade) 100%);
    color: var(--on-colour);
    font-family: "Arimo", Arial, sans-serif;
    font-weight: 400;
    text-transform: uppercase;
  }
  .letterhead .brand-panel { left: 392px; top: 24px; width: 113px; height: 171px; padding: 16px 10px; }
  .brand-name { display: block; font-size: 15px; line-height: 15px; letter-spacing: 0.2px; }
  .brand-sub { display: block; font-size: 7px; line-height: 9px; margin-top: 4px; letter-spacing: 0.3px; }
  .brand-mark { display: block; width: 12px; height: 12px; background: var(--on-colour); margin-bottom: 8px; }

  .letter-body {
    position: absolute; left: 68px; top: 139px; width: 282px;
    font-size: 8.8px; line-height: 9.8px;
  }
  .letter-body p { margin-bottom: 9.8px; }
  .letter-body .salutation { margin-bottom: 12px; }

  .signature { position: absolute; left: 68px; top: 533px; font-size: 8.6px; line-height: 11px; }
  .signature strong { color: var(--ink-strong); font-weight: 700; }

  .contact-panel {
    position: absolute; left: 392px; top: 500px; width: 113px; height: 161px;
    background: linear-gradient(180deg, var(--paper) 0%, var(--red) 30%, var(--red) 100%);
    color: var(--on-colour);
    text-align: right;
    font-size: 8px; line-height: 10px;
    padding: 74px 10px 0 0;
  }
  .contact-panel p + p { margin-top: 6px; }

  .mission {
    position: absolute;
    font-family: "Caveat", cursive;
    color: var(--script);
    font-style: normal;
  }
  .letterhead .mission { left: 68px; top: 612px; font-size: 17px; line-height: 19px; width: 250px; }

  /* Envelope */
  .envelope { left: 611px; top: 513px; width: 539px; height: 269px; }
  .envelope .brand-panel { left: 23px; top: 24px; width: 85px; height: 99px; padding: 11px 7px; }
  .envelope .brand-name { font-size: 11px; line-height: 11px; }
  .envelope .brand-sub { font-size: 5.5px; line-height: 7px; margin-top: 3px; }
  .envelope .brand-mark { width: 9px; height: 9px; margin-bottom: 6px; }

  .recipient {
    position: absolute; left: 227px; top: 108px;
    font-size: 8.6px; line-height: 11.4px; color: var(--ink);
  }
  .recipient strong { font-weight: 700; color: var(--ink-strong); }

  .envelope .mission { left: 26px; top: 233px; font-size: 11.5px; line-height: 13px; white-space: nowrap; }
</style>
</head>
<body>
<main class="stage">

  <section class="sheet letterhead" aria-label="Letterhead">
    <div class="brand-panel">
      <span class="brand-mark"></span>
      <span class="brand-name">Tobin Vale</span>
      <span class="brand-sub">Children's Foundation</span>
    </div>

    <div class="letter-body">
      <p class="salutation">Dear [Name here]</p>
      <p>Lorem ipsum dolor sit amet, consectetur adipiscing elit. Nulla congue mauris ut ligula pharetra fringilla rutrum felis accumsan. Maecenas pulvinar, risus sit amet placerat semper, quam enim porta dui, eu luctus nisi urna in dolor. Pellentesque id eros elementum massa scelerisque suscipit. Phasellus vehicula, lacus ac suscipit consectetur, leo odio molestie sem, sit amet convallis ligula nisi vitae elit. Aliquam id odio non tellus rhoncus scelerisque at a urna.</p>
      <p>Aliquam vel lacus quis lacus blandit dictum ut eu odio. Cum sociis natoque penatibus et magnis dis parturient montes, nascetur ridiculus mus. Fusce dolor enim, tincidunt at tempus a, volutpat quis nibh. Duis lorem neque, vulputate gravida aliquet nec, tincidunt id dolor. Pellentesque vel urna eros. Nulla ultricies, orci vel blandit consectetur, quam ante consequat nibh, ac imperdiet urna est ut lacus. Morbi euismod lobortis tortor, a fermentum lacus varius eu. Vestibulum ante ipsum primis in faucibus orci luctus et ultrices posuere cubilia Curae; Etiam id lorem risus, a mollis ante. Suspendisse malesuada tincidunt est, eu commodo ligula eleifend a.</p>
      <p>Nullam lacinia turpis a orci tristique vitae tristique sem mollis. Maecenas vel varius risus. Praesent imperdiet venenatis faucibus. Fusce volutpat varius diam vitae ullamcorper. Duis vel nunc sapien. Integer faucibus mattis orci, ut feugiat ligula volutpat vitae. Pellentesque porta ipsum at mi bibendum vulputate. Cras quis arcu neque, et semper eros. Maecenas enim sapien, pretium vitae porta mollis, ornare non metus.</p>
      <p>Ut nunc est, gravida id dapibus quis, eleifend et lacus. Cum sociis natoque penatibus et magnis dis parturient montes, nascetur ridiculus mus. Phasellus in neque eros, aliquam consectetur dui.</p>
    </div>

    <div class="signature">
      <strong>Daniel Marsh</strong><br>
      President, Tobin Vale Foundation
    </div>

    <p class="mission">Providing after school enrichment, health, and fitness programs in a safe and nurturing environment...</p>

    <address class="contact-panel">
      <p>PO BOX 315927<br>Harlow Bay,<br>Maine 04915</p>
      <p>P: 877-(TVF)-2815</p>
      <p>E: community@tvfyouth.org</p>
      <p>Web: www.tvfyouth.org</p>
    </address>
  </section>

  <section class="sheet envelope" aria-label="Envelope">
    <div class="brand-panel">
      <span class="brand-mark"></span>
      <span class="brand-name">Tobin Vale</span>
      <span class="brand-sub">Children's Foundation</span>
    </div>

    <address class="recipient">
      <strong>Name [Enter here]</strong><br>
      PO BOX 315927<br>
      Harlow Bay<br>
      Maine<br>
      USA
    </address>

    <p class="mission">Providing after school enrichment, health, and fitness programs in a safe and nurturing environment...</p>
  </section>

</main>
</body>
</html>
```